3 x DIN A4 Flyer, Vorder- und Rückseite
Zielgruppe
Handwerksunternehmen
Aufgabenstellung
Wir benötigen 3 Werbeflyer die in Zeitschriften beigelegt werden. Jeweils DIN A4, Vorderseite beschreibt das Produkt, Rückseite kann zur Bestellung mittels Faxantwort benutzt werden. Profibilder und Text wird vollständig geliefert.

```html
<!DOCTYPE html>
<html lang="de">
<head>
<meta charset="utf-8">
<title>Bestellfax – Planmappe</title>
<link rel="stylesheet" href="https://fonts.googleapis.com/css2?family=Open+Sans:wght@400;600;700;800&display=swap">
<style>
  :root {
    --brand-blue: #1ea8dc;
    --ink: #3b3b3b;
    --ink-dark: #1d1d1b;
    --panel-light: #d6eff9;
    --panel-mid: #aee0f3;
    --field: #ffffff;
    --badge-light: #cdebf7;
    --page-bg: #e6e6e6;
  }
  * { box-sizing: border-box; margin: 0; padding: 0; }
  html, body { width: 933px; height: 1200px; overflow: hidden; }
  body {
    background: var(--page-bg);
    font-family: "Open Sans", Arial, sans-serif;
    color: var(--ink);
    position: relative;
  }
  .flyer {
    position: absolute;
    left: 56px; top: 20px;
    width: 820px; height: 1160px;
    background: #fff;
    overflow: hidden;
  }
  .header {
    position: absolute; left: 0; top: 0; width: 100%; height: 177px;
    background: var(--brand-blue);
  }
  .brand-name {
    position: absolute; left: 66px; top: 64px;
    font-weight: 700; font-size: 38px; line-height: 1; color: var(--ink-dark);
  }
  .doc-title {
    position: absolute; right: 72px; top: 60px;
    font-weight: 800; font-size: 44px; line-height: 1; color: #fff;
  }
  .sender {
    position: absolute; left: 0; top: 177px; width: 100%; height: 265px;
  }
  .sender-company {
    position: absolute; left: 70px; top: 54px;
    font-weight: 700; font-size: 26px;
  }
  .sender-address {
    position: absolute; left: 70px; top: 92px;
    font-weight: 600; font-size: 18px; line-height: 1.4;
  }
  .sender-contact {
    position: absolute; left: 70px; top: 176px;
    font-weight: 600; font-size: 17px;
  }
  .sender-phone {
    position: absolute; right: 72px; top: 172px;
    font-weight: 600; font-size: 22px;
  }
  .fax-badge {
    position: absolute; left: 404px; top: 56px;
    transform: rotate(-4deg); transform-origin: left top;
  }
  .fax-badge-label {
    display: inline-block; background: var(--badge-light);
    font-weight: 700; font-size: 28px; line-height: 1; color: var(--ink);
    padding: 10px 18px 10px 14px; margin-left: 14px;
  }
  .fax-badge-number {
    display: block; background: var(--brand-blue); color: #fff;
    font-weight: 700; font-size: 44px; line-height: 1;
    padding: 8px 18px 12px; width: 352px;
  }
  .details {
    position: absolute; left: 0; top: 442px; width: 100%; height: 396px;
    background: var(--panel-light);
  }
  .section-title {
    position: absolute; left: 70px; top: 40px;
    font-weight: 700; font-size: 21px; color: var(--brand-blue);
  }
  .field {
    position: absolute; height: 36px; background: var(--field);
    border-bottom: 2px solid #4a4a4a;
  }
  .field-label {
    position: absolute; font-size: 15px; font-weight: 400; color: var(--ink);
  }
  .order {
    position: absolute; left: 0; top: 838px; width: 100%; height: 322px;
    background: var(--panel-mid);
  }
  .order-check { position: absolute; left: 66px; top: 58px; }
  .order-text {
    position: absolute; left: 132px; top: 54px;
    font-weight: 700; font-size: 22px; line-height: 1.15; color: var(--ink);
  }
  .order-text span { display: block; }
  .box { position: absolute; background: var(--field); }
</style>
</head>
<body>
  <main class="flyer">
    <header class="header">
      <div class="brand-name">PLANMAPPE</div>
      <h1 class="doc-title">BESTELLFAX</h1>
    </header>

    <section class="sender">
      <div class="sender-company">KLTR mbH</div>
      <div class="sender-address">Lindenhofer Straße 12<br>80331 München</div>
      <div class="sender-contact">Ansprechpartner: Jonas Reiter</div>
      <div class="fax-badge">
        <span class="fax-badge-label">FAX SENDEN AN</span>
        <span class="fax-badge-number">089 47120-100</span>
      </div>
      <div class="sender-phone">Telefon: 089 47120-140</div>
    </section>

    <section class="details">
      <h2 class="section-title">IHRE ANGABEN</h2>
      <div class="field" style="left:70px;top:88px;width:326px"></div>
      <div class="field" style="left:422px;top:88px;width:328px"></div>
      <div class="field-label" style="left:70px;top:132px">Name der Firma</div>
      <div class="field-label" style="left:422px;top:132px">Name, Vorname</div>

      <div class="field" style="left:70px;top:176px;width:326px"></div>
      <div class="field" style="left:422px;top:176px;width:328px"></div>
      <div class="field-label" style="left:70px;top:220px">Straße, Hausnummer</div>
      <div class="field-label" style="left:422px;top:220px">PLZ und Ort</div>

      <div class="field" style="left:70px;top:264px;width:326px"></div>
      <div class="field" style="left:422px;top:264px;width:328px"></div>
      <div class="field-label" style="left:70px;top:312px">Telefon</div>
      <div class="field-label" style="left:422px;top:312px">Sie sind in welcher Innung Mitglied ?</div>
    </section>

    <section class="order">
      <svg class="order-check" width="46" height="46" viewBox="0 0 46 46" aria-hidden="true">
        <rect x="3" y="9" width="32" height="32" fill="#fff" stroke="#3b3b3b" stroke-width="3"/>
        <path d="M10 24 L19 33 L42 4" fill="none" stroke="#1ea8dc" stroke-width="6" stroke-linecap="round" stroke-linejoin="round"/>
      </svg>
      <div class="order-text">
        <span>ICH MÖCHTE DIE</span>
        <span>PLANMAPPE</span>
        <span>BESTELLEN</span>
      </div>
      <div class="field-label" style="left:416px;top:40px">Stückzahl</div>
      <div class="box" style="left:416px;top:66px;width:166px;height:52px"></div>

      <div class="box" style="left:66px;top:176px;width:324px;height:64px"></div>
      <div class="box" style="left:416px;top:176px;width:326px;height:64px"></div>
      <div class="field-label" style="left:66px;top:256px">Ort und Datum</div>
      <div class="field-label" style="left:416px;top:256px">Unterschrift / Stempel</div>
    </section>
  </main>
</body>
</html>
```